Business Card Design

A card that's appealing to realtors and home buyers..
Something that's memorable,attractive, yet simple.

Business

Home Inspection business.
Name of co. Birchline Home Inspections
Serving Kern, Los Angeles, Santa Barbara & Ventura counties
NBPI Certified Inspectors (Use NBPI certified logo)
http://nbpiguild.example/logos/newlogos/NBPI_Logo008.gif
Carl Movrey
661 555-0142
Owen Movrey
805 555-0187
Email :birchlineinspections@mailvero.example
Also use slogan: Providing peace of mind

```html
<!DOCTYPE html>
<html lang="en">
<head>
<meta charset="utf-8">
<title>Birchline Home Inspections – Business Card</title>
<link rel="stylesheet" href="https://fonts.googleapis.com/css2?family=Tinos&family=Arimo:wght@400;700&family=Handlee&display=swap">
<style>
  :root {
    --brand-red: #ee2427;
    --ink: #000000;
    --paper: #ffffff;
    --badge-dark: #1a1a1a;
  }
  html, body {
    margin: 0;
    padding: 0;
    overflow: hidden;
    background: var(--paper);
  }
  .card {
    position: relative;
    width: 1200px;
    height: 702px;
    background: var(--paper);
    overflow: hidden;
    font-family: "Arimo", Arial, sans-serif;
  }
  .card-bands {
    position: absolute;
    inset: 0;
  }
  .company-name {
    position: absolute;
    left: 0;
    width: 1200px;
    top: 104px;
    margin: 0;
    text-align: center;
    font-family: "Tinos", "Times New Roman", serif;
    font-weight: 400;
    font-size: 68px;
    line-height: 80px;
    color: var(--paper);
  }
  .service-area {
    position: absolute;
    left: 0;
    width: 1200px;
    top: 184px;
    margin: 0;
    text-align: center;
    font-size: 26px;
    line-height: 32px;
    color: var(--paper);
  }
  .contact {
    position: absolute;
    left: 56px;
    margin: 0;
  }
  .contact-name {
    display: block;
    font-size: 35px;
    line-height: 40px;
    color: var(--ink);
  }
  .contact-phone {
    display: block;
    font-size: 27px;
    line-height: 34px;
    color: var(--brand-red);
  }
  .contact-carl { top: 326px; }
  .contact-owen { top: 466px; }
  .contact-email {
    position: absolute;
    left: 56px;
    top: 606px;
    margin: 0;
    font-size: 27px;
    line-height: 42px;
    color: var(--ink);
  }
  .contact-email .label {
    font-size: 35px;
    color: var(--brand-red);
    margin-right: 6px;
  }
  .cert-badge {
    position: absolute;
    left: 814px;
    top: 274px;
  }
  .cert-name {
    position: absolute;
    left: 814px;
    top: 486px;
    width: 221px;
    margin: 0;
    text-align: center;
    font-size: 30px;
    line-height: 36px;
    font-weight: 700;
    color: var(--ink);
  }
  .slogan {
    position: absolute;
    left: 749px;
    width: 400px;
    top: 546px;
    margin: 0;
    text-align: center;
    font-family: "Handlee", cursive;
    font-size: 34px;
    line-height: 44px;
    color: var(--ink);
  }
  .insured {
    position: absolute;
    left: 749px;
    width: 400px;
    top: 608px;
    margin: 0;
    text-align: center;
    font-weight: 700;
    font-size: 31px;
    line-height: 38px;
    color: var(--brand-red);
  }
</style>
</head>
<body>
  <main class="card">
    <svg class="card-bands" width="1200" height="702" viewBox="0 0 1200 702" aria-hidden="true">
      <rect x="0" y="0" width="1200" height="236" fill="var(--brand-red)"/>
      <rect x="0" y="236" width="1200" height="16" fill="var(--ink)"/>
      <rect x="0" y="252" width="1200" height="11" fill="var(--brand-red)"/>
      <rect x="0" y="274" width="1200" height="30" fill="var(--brand-red)"/>
      <rect x="814" y="274" width="221" height="30" fill="var(--paper)"/>
    </svg>

    <h1 class="company-name">Birchline Home Inspections</h1>
    <p class="service-area">Serving Kern, Los Angeles, Santa Barbara &amp; Ventura counties</p>

    <p class="contact contact-carl">
      <span class="contact-name">Carl Movrey</span>
      <span class="contact-phone">661 555-0142</span>
    </p>
    <p class="contact contact-owen">
      <span class="contact-name">Owen Movrey</span>
      <span class="contact-phone">805 555-0187</span>
    </p>
    <p class="contact-email"><span class="label">Email:</span>birchlineinspections@mailvero.example</p>

    <svg class="cert-badge" width="221" height="200" viewBox="0 0 221 200" role="img" aria-label="NBPI certification badge">
      <rect x="0" y="0" width="200" height="200" transform="translate(10.5 0)" fill="var(--badge-dark)"/>
    </svg>
    <p class="cert-name">NBPI</p>

    <p class="slogan">Providing peace of mind</p>
    <p class="insured">Insured and Bonded</p>
  </main>
</body>
</html>
```